BrambleWorks business card

Looking for business card design that supports our company/software values. We have 2 logo designs at the moment but open to change if you think you can enhance the brand. Check out website www.brambleworks.com.au.

Target Market(s)

Education

Contact Information for Business Card

Name, title, mobile, email and website

Font styles to use
Sans Serif

Colors

Designer to choose colors to be used in the design.

Requirements
Must have
• BrambleWorks logo with tree and tagline on rear side with dark grey background colour

```html
<!DOCTYPE html>
<html lang="en">
<head>
<meta charset="utf-8">
<title>BrambleWorks business card</title>
<link href="https://fonts.googleapis.com/css2?family=Open+Sans:wght@400;700&family=Ubuntu:wght@400;500&display=swap" rel="stylesheet">
<style>
  :root {
    --page-bg: #d9d9d9;
    --front-top: #3d74aa;
    --front-bottom: #a9c5cc;
    --card-white: #f7f7f7;
    --ink-dark: #4a4a4a;
    --ink-body: #3f3f3f;
    --accent-green: #557a36;
    --accent-coral: #ef5a56;
    --rule-grey: #6b6b6b;
  }
  * { margin: 0; padding: 0; box-sizing: border-box; }
  html, body {
    width: 1200px; height: 1200px; overflow: hidden;
    background: var(--page-bg);
  }
  .canvas { position: relative; width: 1200px; height: 1200px; }

  .card {
    position: absolute;
    left: 222px;
    width: 754px; height: 434px;
    border-radius: 32px;
    overflow: hidden;
  }

  /* Front side */
  .card-front {
    top: 104px;
    background: linear-gradient(180deg, var(--front-top) 0%, var(--front-bottom) 100%);
  }
  .front-mark {
    position: absolute; left: 0; right: 0; top: 150px;
    display: flex; align-items: center; justify-content: center; gap: 16px;
  }
  .front-mark .mark-dot {
    width: 46px; height: 46px; border-radius: 50%;
    background: var(--ink-dark);
  }
  .front-mark .mark-name {
    font-family: "Ubuntu", sans-serif; font-weight: 500;
    font-size: 48px; color: var(--ink-dark);
  }
  .front-url {
    position: absolute; left: 0; right: 0; top: 376px;
    text-align: center;
    font-family: "Open Sans", sans-serif; font-size: 21px;
    color: var(--accent-coral);
  }

  /* Back side */
  .card-back {
    top: 604px;
    background: var(--card-white);
  }
  .brand-block { position: absolute; left: 28px; top: 48px; display: flex; align-items: center; gap: 20px; }
  .brand-dot { width: 92px; height: 92px; border-radius: 50%; background: var(--ink-dark); }
  .brand-text { display: flex; flex-direction: column; }
  .brand-name {
    font-family: "Ubuntu", sans-serif; font-weight: 400;
    font-size: 43px; line-height: 1.1; color: var(--ink-dark);
    border-bottom: 1.5px solid var(--rule-grey); padding-bottom: 6px;
  }
  .brand-tagline {
    font-family: "Ubuntu", sans-serif; font-size: 18.5px;
    color: var(--ink-dark); padding: 5px 0 0 6px;
  }

  .person-name {
    position: absolute; right: 30px; top: 172px;
    font-family: "Open Sans", sans-serif; font-weight: 700;
    font-size: 30px; color: var(--accent-green);
  }
  .name-bar {
    position: absolute; right: 0; top: 179px;
    width: 11px; height: 51px; background: var(--accent-green);
  }
  .title-rule {
    position: absolute; left: 27px; top: 222px;
    width: 608px; height: 1.5px; background: var(--rule-grey);
  }
  .person-title {
    position: absolute; right: 30px; top: 207px;
    font-family: "Open Sans", sans-serif; font-size: 20px;
    color: var(--ink-body);
  }

  .address {
    position: absolute; left: 25px; top: 250px;
    font-family: "Open Sans", sans-serif; font-size: 19.5px;
    line-height: 28px; color: var(--ink-body);
  }
  .contacts {
    position: absolute; left: 25px; top: 328px;
    list-style: none;
    font-family: "Open Sans", sans-serif; font-size: 19.5px;
    color: var(--ink-body);
  }
  .contacts li { display: flex; align-items: center; height: 28px; }
  .contacts svg { width: 16px; height: 16px; margin-right: 11px; fill: var(--accent-green); }

  .corner-accent {
    position: absolute; right: -40px; bottom: -40px;
    width: 190px; height: 190px; border-radius: 50%;
    background: #e9ebe6;
  }
</style>
</head>
<body>
<main class="canvas">

  <section class="card card-front" aria-label="Card front">
    <div class="front-mark">
      <span class="mark-dot"></span>
      <span class="mark-name">BrambleWorks</span>
    </div>
    <p class="front-url">www.brambleworks.com.au</p>
  </section>

  <section class="card card-back" aria-label="Card back">
    <div class="corner-accent"></div>

    <div class="brand-block">
      <span class="brand-dot"></span>
      <div class="brand-text">
        <span class="brand-name">BrambleWorks</span>
        <span class="brand-tagline">Student Success Platform</span>
      </div>
    </div>

    <p class="person-name">Daniel Reeve</p>
    <div class="name-bar"></div>
    <div class="title-rule"></div>
    <p class="person-title">Founder</p>

    <p class="address">P.O. Box: 48210, Linden Row Street<br>Bristol, United Kingdom</p>

    <ul class="contacts">
      <li>
        <svg viewBox="0 0 24 24" aria-hidden="true"><path d="M6.6 10.8a15.1 15.1 0 0 0 6.6 6.6l2.2-2.2c.3-.3.7-.4 1-.2 1.1.4 2.3.6 3.6.6.6 0 1 .4 1 1V20c0 .6-.4 1-1 1A17 17 0 0 1 3 4c0-.6.4-1 1-1h3.5c.6 0 1 .4 1 1 0 1.3.2 2.5.6 3.6.1.3 0 .7-.2 1z"/></svg>
        555-214-7788
      </li>
      <li>
        <svg viewBox="0 0 24 24" aria-hidden="true"><path d="M2 5h20v14H2z M4 7v.4l8 5.2 8-5.2V7z" fill-rule="evenodd"/></svg>
        info@brambleworks.com.au
      </li>
      <li>
        <svg viewBox="0 0 24 24" aria-hidden="true"><circle cx="12" cy="12" r="10"/><path d="M2 12h20M12 2c3 3 3 17 0 20M12 2c-3 3-3 17 0 20" stroke="#f7f7f7" stroke-width="1.6" fill="none"/></svg>
        www.brambleworks.com.au
      </li>
    </ul>
  </section>

</main>
</body>
</html>
```